Brightwell Support! Virtual Assistant business needs a Website

I have started an online business called "Brightwell Support". I offer all the same types of services as a typical Personal Assistant, only remotely. For example, document formatting and editing (word, powerpoint, excel etc.), email and calendar management, appointments and bookings, document creation, reports, travel and event management and so on.

I already have a logo ready to go, however I have yet to finalise the copy for the site, so if you could create the pages with pictures, and I can fill in the wording at a later date.

Target Market(s)

Anyone who is overloaded at work and needs someone to take the admin work off their hands.

Number of Pages Required

4 page

Font styles to use
Sans Serif
Script
Other font styles liked:
• Gotham Medium is used in my font

Colors

Designer to choose colors to be used in the design.

Requirements
Must have
• Home Page
• About Page
• Pricing Page
• Contact Page
Nice to have
• Pictures and a professional design, I like white space and simple design.
Should not have
• cartoons or anything unprofessional looking.

```html
<!DOCTYPE html>
<html lang="en">
<head>
<meta charset="utf-8">
<title>Brightwell Support</title>
<link rel="stylesheet" href="https://fonts.googleapis.com/css2?family=Montserrat:wght@400;500;600;700&family=Raleway:wght@400;500;600&display=swap">
<style>
:root{
  --blue-deep:#1b4fa3;
  --blue:#1f6cc6;
  --blue-bright:#1a8ad8;
  --blue-mid:#3d7bc4;
  --blue-light:#6aaee0;
  --navy:#17479a;
  --grey-btn:#8a8a8a;
  --grey-text:#6f6f6f;
  --ink:#333;
  --paper:#f6f6f6;
  --white:#fff;
}
*{box-sizing:border-box;margin:0;padding:0}
html,body{width:1200px;height:3232px;overflow:hidden}
body{position:relative;background:var(--paper);font-family:"Raleway",sans-serif;color:var(--ink)}
.abs{position:absolute}
h1,h2,h3,.brand,.btn,.plan-name,.plan-price{font-family:"Montserrat",sans-serif}
.btn{display:inline-block;background:var(--grey-btn);color:var(--white);font-weight:600;font-size:14px;padding:11px 25px;border-radius:20px 4px 20px 4px;text-decoration:none}

/* header */
.site-header{left:0;top:0;width:1200px;height:86px;background:var(--white);box-shadow:0 2px 8px rgba(0,0,0,.08);z-index:5}
.brand{left:104px;top:26px;display:flex;align-items:center;gap:10px;font-size:26px;font-weight:600;color:var(--navy)}
.brand-dot{width:34px;height:34px;border-radius:50%;background:var(--navy)}
.main-nav{left:600px;top:36px;display:flex;gap:40px;font-size:13px;font-weight:600;font-family:"Montserrat",sans-serif}
.main-nav a{color:#222;text-decoration:none;position:relative}
.main-nav a.active::after{content:"";position:absolute;left:-10px;right:-10px;top:48px;height:2px;background:#999}
.social{left:950px;top:24px;display:flex;gap:10px}
.social span{width:38px;height:38px;border-radius:50%;background:var(--white);box-shadow:0 1px 5px rgba(0,0,0,.2)}

/* hero */
.hero-bg{left:0;top:86px;width:1200px;height:560px}
.hero-title{left:0;top:170px;width:1200px;text-align:center;color:var(--white);font-size:40px;font-weight:500}
.hero-sub{left:0;top:224px;width:1200px;text-align:center;color:#e4efff;font-size:13px}
.hero-btn{left:537px;top:268px}
.hero-art{left:225px;top:305px;width:750px;height:335px;border-radius:20px;background:radial-gradient(ellipse at center,rgba(220,230,245,.55),rgba(120,160,220,.15) 70%,transparent)}
.hero-dots{left:1066px;top:320px;display:flex;flex-direction:column;gap:10px}
.hero-dots span{width:10px;height:10px;border:2px solid var(--white)}

/* welcome */
.welcome-title{left:0;top:690px;width:1200px;text-align:center;font-size:40px;font-weight:500;color:var(--grey-text)}
.welcome-title b,.works-title b{color:var(--navy);font-weight:600}
.welcome-text{left:205px;top:758px;width:790px;text-align:center;font-size:11.5px;line-height:22px;color:#555}
.welcome-btn{left:537px;top:850px}

/* services */
.services-bg{left:0;top:860px;width:1200px;height:660px}
.services-title{left:0;top:918px;width:1200px;text-align:center;font-size:38px;font-weight:500;color:var(--grey-text)}
.service{width:340px;text-align:center;color:var(--white)}
.service-icon{width:184px;height:184px;border-radius:50%;background:var(--white);margin:0 auto;display:flex;align-items:center;justify-content:center}
.service h3{margin-top:32px;font-size:16px;font-weight:600}
.service p{margin-top:12px;font-size:11.5px;line-height:22px;color:#e3eefc}
.services-btn{left:502px;top:1402px}

/* how it works */
.works-media{left:105px;top:1550px;width:478px;height:352px;border-radius:20px;box-shadow:0 8px 20px rgba(0,0,0,.25);background:linear-gradient(135deg,#b88a6e,#d8c3b0 45%,#e9ece9 75%,#c9c2b8)}
.play{left:315px;top:1710px;width:54px;height:54px;border-radius:50%;background:#e2262b}
.works-title{left:610px;top:1585px;font-size:38px;font-weight:500;color:var(--grey-text)}
.works-text{left:612px;top:1652px;width:485px;font-size:11.5px;line-height:22px;color:#555}
.works-btn{left:610px;top:1788px}

/* pricing */
.pricing-bg{left:0;top:1960px;width:1200px;height:700px}
.pricing-title{left:0;top:2045px;width:1200px;text-align:center;font-size:38px;font-weight:500;color:var(--grey-text)}
.plan{top:2130px;width:296px;height:420px;background:#ededed;border-radius:28px 6px 28px 6px}
.plan-head{height:128px;border-radius:28px 6px 28px 6px;color:var(--white);text-align:center;padding-top:18px}
.plan-name{font-size:26px;font-weight:500}
.plan-price{font-size:38px;font-weight:600;margin-top:2px}
.plan-price sup{font-size:18px;vertical-align:18px}
.plan ul{list-style:none;padding:0 6px}
.plan li{height:47px;line-height:47px;text-align:center;font-size:13px;color:#444;border-bottom:1px solid #d6d6d6}
.plan li:last-child{border-bottom:none}
.plan .btn{position:absolute;left:84px;bottom:-20px}
.basic .plan-head{background:var(--navy)}
.standard .plan-head{background:var(--blue-mid)}
.advanced .plan-head{background:var(--blue-light)}

/* contact */
.footer-bg{left:0;top:2640px;width:1200px;height:540px}
.contact-card{left:97px;top:2832px;width:273px;height:278px;background:rgba(20,60,140,.55)}
.contact-row{display:flex;align-items:center;gap:18px;height:92px;padding-left:18px;border-bottom:1px solid rgba(255,255,255,.15);color:var(--white);font-size:12px;line-height:20px}
.contact-row:last-child{border-bottom:none}
.contact-icon{flex:none;width:48px;height:48px;border-radius:50%;background:#8f9bb0;display:flex;align-items:center;justify-content:center}
.contact-title{left:507px;top:2810px;font-size:38px;font-weight:500;color:var(--white)}
.field{border:1px solid #5d9ae0;background:rgba(40,110,200,.35);color:#dbe8fa;font-size:11px;padding:8px 10px}
.submit{left:520px;top:3080px;padding:11px 40px}
.copyright{left:0;top:3180px;width:1200px;height:52px;background:var(--navy);color:#dce7f7;font-size:12px;text-align:center;line-height:52px}
</style>
</head>
<body>

<header class="site-header abs">
  <div class="brand abs"><span class="brand-dot"></span>Brightwell Support</div>
  <nav class="main-nav abs">
    <a class="active" href="#">Home</a><a href="#">About us</a><a href="#">Pricing</a><a href="#">Contact Us</a>
  </nav>
  <div class="social abs" aria-label="Social links"><span></span><span></span><span></span></div>
</header>

<svg class="hero-bg abs" viewBox="0 0 1200 560" preserveAspectRatio="none" aria-hidden="true">
  <defs><linearGradient id="heroGrad" x1="0" y1="0" x2="1" y2="0.3">
    <stop offset="0" stop-color="#1b4fa3"/><stop offset="1" stop-color="#1290dc"/></linearGradient></defs>
  <rect width="1200" height="560" fill="url(#heroGrad)"/>
  <path d="M0 460 C200 400 380 400 600 470 C800 530 1000 500 1200 430 L1200 560 L0 560Z" fill="#5a9ad8" opacity=".5"/>
  <path d="M0 490 C220 440 420 470 620 510 C820 545 1020 520 1200 470 L1200 560 L0 560Z" fill="var(--paper)"/>
</svg>
<h1 class="hero-title abs">Brightwell Support</h1>
<p class="hero-sub abs">Remote admin help so you can focus on the work that matters.</p>
<a class="btn hero-btn abs" href="#">Get Started</a>
<div class="hero-art abs" role="img" aria-label="Two laptops surrounded by floating document, calendar and email icons"></div>
<div class="hero-dots abs"><span></span><span></span><span></span></div>

<h2 class="welcome-title abs">Welcome To <b>Brightwell Support</b></h2>
<p class="welcome-text abs">We take the everyday admin off your desk so you can get back to the work you love. From inbox triage to document formatting, bookings and reports, our remote assistants handle the details with care, speed and discretion. Flexible plans suit busy professionals and growing teams alike, with clear pricing and friendly support.</p>
<a class="btn welcome-btn abs" href="#">Read More</a>

<svg class="services-bg abs" viewBox="0 0 1200 660" preserveAspectRatio="none" aria-hidden="true">
  <defs><linearGradient id="svcGrad" x1="0" y1="0" x2="1" y2="0">
    <stop offset="0" stop-color="#1b4fa3"/><stop offset="1" stop-color="#1a8ad8"/></linearGradient></defs>
  <path d="M0 20 Q600 360 1200 20 L1200 540 C1000 600 820 620 600 560 C380 500 200 520 0 560Z" fill="url(#svcGrad)"/>
  <path d="M0 20 Q600 360 1200 20 L1200 70 Q600 380 0 70Z" fill="#6aaee0" opacity=".6"/>
  <path d="M0 520 C220 470 420 500 620 540 C820 580 1020 560 1200 500 L1200 560 C1000 640 820 650 600 600 C400 550 200 560 0 580Z" fill="#6aaee0" opacity=".7"/>
</svg>
<h2 class="services-title abs">Services</h2>

<div class="service abs" style="left:80px;top:988px">
  <div class="service-icon"><svg width="62" height="46" viewBox="0 0 62 46"><rect x="3" y="3" width="56" height="40" rx="3" fill="none" stroke="#2f4a7a" stroke-width="5"/><path d="M5 6 L31 27 L57 6" fill="none" stroke="#2f4a7a" stroke-width="5"/></svg></div>
  <h3>Email management</h3>
  <p>We sort, reply to and organise your inbox daily so urgent messages never slip past you again.</p>
</div>
<div class="service abs" style="left:430px;top:988px">
  <div class="service-icon"><svg width="50" height="54" viewBox="0 0 50 54"><rect x="3" y="7" width="44" height="44" rx="4" fill="none" stroke="#2f4a7a" stroke-width="5"/><rect x="11" y="1" width="5" height="10" fill="#2f4a7a"/><rect x="34" y="1" width="5" height="10" fill="#2f4a7a"/><rect x="3" y="7" width="44" height="9" fill="#2f4a7a"/><g fill="#2f4a7a"><rect x="11" y="22" width="7" height="7"/><rect x="22" y="22" width="7" height="7"/><rect x="33" y="22" width="7" height="7"/><rect x="11" y="33" width="7" height="7"/><rect x="22" y="33" width="7" height="7"/><rect x="33" y="33" width="7" height="7"/></g></svg></div>
  <h3>Calendar management</h3>
  <p>Meetings, reminders and deadlines kept in order, with every clash spotted and solved early.</p>
</div>
<div class="service abs" style="left:782px;top:988px">
  <div class="service-icon"><svg width="56" height="56" viewBox="0 0 56 56"><circle cx="28" cy="28" r="24" fill="none" stroke="#2f4a7a" stroke-width="5"/><path d="M16 29 L25 38 L41 20" fill="none" stroke="#2f4a7a" stroke-width="5"/></svg></div>
  <h3>Appointments and bookings</h3>
  <p>Travel, venues and appointments booked and confirmed, with all details sent straight to you.</p>
</div>
<a class="btn services-btn abs" href="#">View More Services</a>

<div class="works-media abs" role="img" aria-label="Photo of a small team working together at a café table with a tablet and laptop"></div>
<svg class="play abs" viewBox="0 0 54 54" aria-hidden="true"><circle cx="27" cy="27" r="27" fill="#e2262b"/><path d="M21 16 L38 27 L21 38Z" fill="#fff"/></svg>
<h2 class="works-title abs">How it <b>Works</b></h2>
<p class="works-text abs">Tell us what is weighing on your week and we match you with a dedicated assistant. Together we agree on priorities, tools and how you like to communicate. Tasks are tracked in one shared list, and you get a short update at the end of each day. Add or change work whenever you need, with no long contracts.</p>
<a class="btn works-btn abs" href="#">Read More</a>

<svg class="pricing-bg abs" viewBox="0 0 1200 700" preserveAspectRatio="none" aria-hidden="true">
  <path d="M0 40 C250 0 450 10 650 40 C850 70 1050 50 1200 20 L1200 700 L0 700Z" fill="#eeeeee"/>
</svg>
<h2 class="pricing-title abs">Pricing</h2>

<div class="plan basic abs" style="left:108px">
  <div class="plan-head"><div class="plan-name">Basic</div><div class="plan-price"><sup>$</sup>49</div></div>
  <ul><li>Up to 10 users monthly</li><li>Unlimited updates</li><li>Free Documents</li><li>24/7 Support</li><li>10 Unique Users</li></ul>
  <a class="btn" href="#">Select Plan</a>
</div>
<div class="plan standard abs" style="left:451px">
  <div class="plan-head"><div class="plan-name">Standard</div><div class="plan-price"><sup>$</sup>69</div></div>
  <ul><li>Up to 10 users monthly</li><li>Unlimited updates</li><li>Free Documents</li><li>24/7 Support</li><li>10 Unique Users</li></ul>
  <a class="btn" href="#">Select Plan</a>
</div>
<div class="plan advanced abs" style="left:798px">
  <div class="plan-head"><div class="plan-name">Advanced</div><div class="plan-price"><sup>$</sup>99</div></div>
  <ul><li>Up to 10 users monthly</li><li>Unlimited updates</li><li>Free Documents</li><li>24/7 Support</li><li>10 Unique Users</li></ul>
  <a class="btn" href="#">Select Plan</a>
</div>

<svg class="footer-bg abs" viewBox="0 0 1200 540" preserveAspectRatio="none" aria-hidden="true">
  <defs><linearGradient id="footGrad" x1="0" y1="0" x2="1" y2="0">
    <stop offset="0" stop-color="#1b4fa3"/><stop offset="1" stop-color="#1a86d4"/></linearGradient></defs>
  <path d="M0 70 C200 10 400 10 600 60 C800 110 1000 90 1200 30 L1200 540 L0 540Z" fill="#4d8fd6"/>
  <path d="M0 110 C220 60 420 70 620 110 C820 150 1020 130 1200 80 L1200 540 L0 540Z" fill="url(#footGrad)"/>
</svg>

<div class="contact-card abs">
  <div class="contact-row"><span class="contact-icon"><svg width="20" height="26" viewBox="0 0 20 26"><path d="M10 1 C4 1 1 5 1 10 C1 17 10 25 10 25 C10 25 19 17 19 10 C19 5 16 1 10 1Z" fill="#fff"/><circle cx="10" cy="10" r="3.5" fill="#8f9bb0"/></svg></span><span>Brightwell Support<br>#48 Harbour Lane,<br>Sydney, AU</span></div>
  <div class="contact-row"><span class="contact-icon"><svg width="22" height="22" viewBox="0 0 22 22"><path d="M5 1 L9 6 L7 9 C8 12 10 14 13 15 L16 13 L21 17 L18 21 C9 21 1 13 1 4Z" fill="#fff"/></svg></span><span>1-800 555 0142</span></div>
  <div class="contact-row"><span class="contact-icon"><svg width="24" height="18" viewBox="0 0 24 18"><rect x="1" y="1" width="22" height="16" rx="2" fill="#fff"/><path d="M2 2 L12 10 L22 2" fill="none" stroke="#8f9bb0" stroke-width="2"/></svg></span><span>hello@brightwellsupport.com</span></div>
</div>

<h2 class="contact-title abs">Contact Us</h2>
<div class="field abs" style="left:513px;top:2898px;width:284px;height:36px">Name</div>
<div class="field abs" style="left:808px;top:2898px;width:285px;height:36px">Email</div>
<div class="field abs" style="left:513px;top:2948px;width:580px;height:36px">Subject</div>
<div class="field abs" style="left:513px;top:3000px;width:580px;height:66px">Message</div>
<a class="btn submit abs" href="#">Submit</a>

<footer class="copyright abs">© 2018 Copyright &nbsp;|&nbsp; brightwellsupport.com - All Rights Reserved.</footer>

</body>
</html>
```